Aesthetics Company Flyer (description of services)

We need a 5.5"x8.5" flyer describing the services we offer at radiant meadowbrook aesthetics. We are an aesthetics company located in Conroe TX. Our products and services can be found at www.rmaesthetica.example/services . We would like to see designs that are cohesive with our brand and website: https://www.rmaesthetica.example/

```html
<!DOCTYPE html>
<html lang="en">
<head>
<meta charset="utf-8">
<title>Radiant Meadowbrook Aesthetics – Services Flyer</title>
<link rel="stylesheet" href="https://fonts.googleapis.com/css2?family=Cinzel:wght@400&family=Oswald:wght@400&family=Roboto+Condensed:wght@300;400&display=swap">
<style>
  :root{
    --lavender:#ddd4e7;
    --lavender-deep:#b4a7d0;
    --blush:#f3c3cf;
    --blush-soft:#f8e1e6;
    --plum:#86689f;
    --plum-text:#8a6ea4;
    --ink:#3b3440;
    --rose:#e9779f;
    --sky:#6cc6ee;
    --sky-deep:#1d9ed9;
    --sky-pale:#b7e0f1;
    --white:#ffffff;
  }
  *{box-sizing:border-box;margin:0;padding:0}
  html,body{width:776px;height:1200px;overflow:hidden;background:var(--white)}
  .flyer{position:relative;width:776px;height:1200px;overflow:hidden;background:var(--lavender);font-family:"Roboto Condensed",sans-serif}
  .backdrop{position:absolute;inset:0}
  .hero-photo{position:absolute;left:282px;top:0;width:494px;height:300px;
    background:radial-gradient(ellipse at 70% 40%,rgba(196,140,150,.55),rgba(230,190,200,.35) 45%,rgba(250,230,235,0) 75%);}
  .brand-mark{position:absolute;left:62px;top:120px;width:215px;text-align:center;color:var(--plum)}
  .brand-mark .dot{display:block;width:70px;height:70px;border-radius:50%;margin:0 auto 14px;background:var(--blush)}
  .brand-mark .name{font-family:"Roboto Condensed",sans-serif;font-weight:400;font-size:17px;letter-spacing:2px;text-transform:uppercase;line-height:1.3}
  .title{position:absolute;left:287px;top:78px;font-family:"Cinzel",serif;font-weight:400;color:var(--white);font-size:56px;line-height:62px;text-shadow:2px 3px 3px rgba(90,70,90,.55)}
  .title span{display:block}
  .tagline{position:absolute;left:287px;top:220px;font-family:"Cinzel",serif;font-size:17.5px;line-height:25px;color:var(--plum-text)}
  .intro{position:absolute;left:70px;top:324px;width:640px;font-size:19.5px;line-height:29.6px;color:var(--plum-text);font-weight:400}
  .lead-bar{display:inline-block;width:46px;height:15px;margin-right:6px;vertical-align:-1px;background:var(--lavender-deep)}
  .service{position:absolute;top:484px;width:303px}
  .service--weight{left:70px}
  .service--neuro{left:403px}
  .service-photo{position:relative;height:252px;border:2px solid var(--rose);border-bottom-right-radius:46px;border-top-left-radius:0;overflow:hidden}
  .service--weight .service-photo{background:linear-gradient(135deg,#d9a07a 0%,#c98a5e 45%,#8a6a58 75%,#e5cbbd 100%)}
  .service--neuro .service-photo{border-color:var(--sky);background:linear-gradient(135deg,#e9e6ea 0%,#c9a08a 40%,#7a5648 60%,#efeef0 100%)}
  .badge{position:absolute;left:-16px;top:52px;width:46px;height:46px;border-radius:50%;background:var(--white)}
  .service-title{position:absolute;left:14px;bottom:14px;font-family:"Oswald",sans-serif;font-weight:400;color:var(--white);font-size:38px;line-height:1;text-shadow:1px 2px 3px rgba(0,0,0,.35)}
  .service--neuro .service-title{left:20px;bottom:38px}
  .service-sub{position:absolute;left:20px;bottom:10px;font-family:"Oswald",sans-serif;color:var(--sky-deep);font-size:20px;line-height:1}
  .service-text{margin-top:15px;font-size:19.5px;line-height:28.2px;color:var(--ink);font-weight:400}
  .service-text .bar{display:inline-block;width:46px;height:15px;margin-right:6px;vertical-align:-1px}
  .service--weight .bar{background:var(--rose)}
  .service--neuro .bar{background:var(--sky-pale)}
  .treatments{list-style:none;margin-top:14px}
  .treatments li{font-size:19.5px;line-height:28.5px;color:var(--plum-text);text-transform:uppercase}
  .treatments li::before{content:"";display:inline-block;width:10px;height:10px;margin-right:6px;background:var(--sky-deep);vertical-align:1px}
  .contact{position:absolute;left:70px;top:1060px;color:var(--plum)}
  .contact .phone{font-family:"Oswald",sans-serif;font-size:44px;line-height:48px}
  .contact .email{font-family:"Roboto Condensed",sans-serif;font-weight:300;font-size:17px;letter-spacing:3px;line-height:22px;margin-top:4px}
  .contact .web{font-family:"Oswald",sans-serif;font-size:44px;letter-spacing:4.5px;line-height:48px}
</style>
</head>
<body>
<main class="flyer">
  <svg class="backdrop" width="776" height="1200" viewBox="0 0 776 1200" aria-hidden="true">
    <defs>
      <linearGradient id="topFade" x1="0" y1="0" x2="1" y2="0.4">
        <stop offset="0" stop-color="#ffffff"/>
        <stop offset="0.45" stop-color="#fbeef2"/>
        <stop offset="1" stop-color="#eec7d2"/>
      </linearGradient>
    </defs>
    <path d="M0 0H776V300C650 260 520 275 400 300C260 330 150 360 0 345Z" fill="url(#topFade)"/>
    <path d="M0 440C120 470 260 470 420 455C560 440 680 420 776 428V300C650 290 520 300 400 320C260 345 120 360 0 350Z" fill="#e4d9ea" opacity=".6"/>
    <path d="M0 1020C110 1005 210 1040 330 1085C470 1135 620 1150 776 1142V1200H0Z" fill="var(--blush)"/>
  </svg>

  <div class="hero-photo" role="img" aria-label="Soft-focus portrait photograph of a smiling woman fading into the pink background"></div>

  <div class="brand-mark">
    <span class="dot"></span>
    <span class="name">Radiant Meadowbrook Aesthetics</span>
  </div>

  <h1 class="title"><span>Radiant</span><span>Meadowbrook</span></h1>
  <p class="tagline">Everyone is beautiful.<br>With us, everyone can feel<br>beautiful too</p>

  <p class="intro"><span class="lead-bar"></span>At Radiant Meadowbrook Aesthetics we offer a comprehensive list of aesthetic, skincare and weight loss services and IV hydration therapy. But before you embark on your journey with us, you must first book a consultation so we can assess and understand your needs and decide on the best option to address those needs.</p>

  <section class="service service--weight">
    <div class="service-photo" role="img" aria-label="Close-up photograph of a weight loss injection pen">
      <h2 class="service-title">Weightloss</h2>
    </div>
    <span class="badge"></span>
    <p class="service-text"><span class="bar"></span>Semaglutide stimulates insulin to be released from the pancreas in an effort to slow down gastric emptying and inhibits inappropriate release of sugars after we eat. Simply put, this process ultimately reduces our food intake from within, thereby leading to weight loss.</p>
  </section>

  <section class="service service--neuro">
    <div class="service-photo" role="img" aria-label="Photograph of a gloved practitioner giving a facial injection">
      <h2 class="service-title">Neurotoxin</h2>
      <span class="service-sub">Wrinkle Relaxer</span>
    </div>
    <span class="badge"></span>
    <p class="service-text"><span class="bar"></span>Neurotoxin injections lessens facial lines that can give you a tired appearance. These lines are produced by repeated muscle contractions most noticeable on the forehead, between the eyebrows and around the eyes. Smoothara® relaxes these muscles to give the skin a smooth appearance. (Smoothara®, Calmiva®, Lumitox®)</p>
    <ul class="treatments">
      <li>Wrinkle Relaxer</li>
      <li>Lip Flip</li>
    </ul>
  </section>

  <address class="contact" style="font-style:normal">
    <div class="phone">936 555 0148</div>
    <div class="email">hello@rmaesthetica.example</div>
    <div class="web">www.rmaesthetica.example</div>
  </address>
</main>
</body>
</html>
```